Business Card design for new private practice opening

I need a business card design for my new private practice with my new logo uploaded as a file
On the front the logo
On the back: maybe a small logo somewhere?
Priv. Doz. DDr. Corinna Vestaluk
Fachärztin für Allgemein- & Viszeralchirurgie
Address: xxx
Tel: xxx
Mobil:xxx
Webseite:xxx
Email:xxx

Contact Information for Business Card

See project description above for details

Requirements
Nice to have
• I would like the colors of the logo incorporated into the business card

```html
<!DOCTYPE html>
<html lang="de">
<head>
<meta charset="utf-8">
<title>Vestaluk Chirurgie – Visitenkarte</title>
<link href="https://fonts.googleapis.com/css2?family=Figtree:wght@400;500;700&display=swap" rel="stylesheet">
<style>
  :root {
    --backdrop: #e6e8e7;
    --card: #f7f7f7;
    --teal: #36a9a3;
    --grey-logo: #6f6f6f;
    --ink: #404040;
  }
  html, body {
    margin: 0;
    width: 1200px;
    height: 1200px;
    overflow: hidden;
    background: var(--backdrop);
    font-family: "Figtree", Arial, sans-serif;
  }
  .card {
    position: absolute;
    left: 255px;
    width: 728px;
    height: 416px;
    background: var(--card);
    border-radius: 4px;
    box-shadow: 0 2px 10px rgba(0,0,0,0.08);
  }
  .card--contact { top: 134px; }
  .card--brand { top: 610px; }

  .contact__mark {
    position: absolute;
    left: 551px;
    top: 65px;
    width: 102px;
    height: 102px;
    border: 3px solid var(--grey-logo);
    border-radius: 50%;
    box-sizing: border-box;
  }
  .contact__name {
    position: absolute;
    left: 69px;
    top: 168px;
    margin: 0;
    font-size: 27px;
    font-weight: 700;
    color: var(--teal);
    white-space: nowrap;
  }
  .contact__title {
    position: absolute;
    left: 69px;
    top: 202px;
    margin: 0;
    font-size: 18.5px;
    font-weight: 500;
    color: var(--ink);
    letter-spacing: 0.2px;
    white-space: nowrap;
  }
  .contact__rule {
    position: absolute;
    left: 69px;
    top: 236px;
    width: 592px;
    height: 3px;
    background: var(--teal);
  }
  .contact__row {
    position: absolute;
    display: flex;
    align-items: center;
    font-size: 18.5px;
    color: var(--ink);
    white-space: nowrap;
    line-height: 1;
  }
  .contact__row svg {
    width: 16px;
    height: 16px;
    margin-right: 9px;
    fill: var(--teal);
    flex: none;
  }
  .row-phone { left: 69px; top: 254px; }
  .row-mobile { left: 69px; top: 280px; }
  .row-mail { left: 69px; top: 307px; }
  .row-web { left: 69px; top: 331px; }
  .row-address { left: 415px; top: 307px; align-items: flex-start; line-height: 25px; margin-top: -5px; }
  .row-address svg { margin-top: 3px; height: 19px; width: 16px; margin-right: 8px; }

  .brand {
    position: absolute;
    left: 153px;
    top: 146px;
    display: flex;
    align-items: center;
  }
  .brand__mark {
    width: 124px;
    height: 124px;
    border: 4px solid var(--grey-logo);
    border-radius: 50%;
    box-sizing: border-box;
    margin-right: 19px;
  }
  .brand__name {
    margin: 0;
    font-size: 48px;
    font-weight: 700;
    line-height: 52px;
    color: var(--grey-logo);
    letter-spacing: 1px;
  }
</style>
</head>
<body>

<section class="card card--contact">
  <div class="contact__mark"></div>
  <h1 class="contact__name">Priv. Doz. DDr. Corinna Vestaluk</h1>
  <p class="contact__title">Fachärztin für Allgemein- &amp; Viszeralchirurgie</p>
  <div class="contact__rule"></div>

  <div class="contact__row row-phone">
    <svg viewBox="0 0 24 24"><path d="M6.6 10.8a15.1 15.1 0 0 0 6.6 6.6l2.2-2.2c.3-.3.7-.4 1-.2 1.1.4 2.3.6 3.6.6.6 0 1 .4 1 1V20c0 .6-.4 1-1 1A17 17 0 0 1 3 4c0-.6.4-1 1-1h3.5c.6 0 1 .4 1 1 0 1.3.2 2.5.6 3.6.1.3 0 .7-.2 1z"/></svg>
    (211) 47391
  </div>
  <div class="contact__row row-mobile">
    <svg viewBox="0 0 24 24"><path d="M7 1h10a2 2 0 0 1 2 2v18a2 2 0 0 1-2 2H7a2 2 0 0 1-2-2V3a2 2 0 0 1 2-2zm0 3v14h10V4zm5 15.3a1.1 1.1 0 1 0 0 2.2 1.1 1.1 0 0 0 0-2.2z"/></svg>
    (211) 630582
  </div>
  <div class="contact__row row-mail">
    <svg viewBox="0 0 24 24"><path d="M2 5h20v14H2zm2 2v.4l8 5.2 8-5.2V7zm0 2.8V17h16V9.8l-8 5.2z"/></svg>
    info@vestalukchirurgie.com
  </div>
  <div class="contact__row row-web">
    <svg viewBox="0 0 24 24"><path d="M12 2a10 10 0 1 0 0 20 10 10 0 0 0 0-20zm6.9 6h-3a15 15 0 0 0-1.3-3.9A8 8 0 0 1 18.9 8zM12 4c.8 1.2 1.5 2.5 1.9 4h-3.8c.4-1.5 1.1-2.8 1.9-4zM4.3 14a8.2 8.2 0 0 1 0-4h3.4a16 16 0 0 0 0 4zm.8 2h3a15 15 0 0 0 1.3 3.9A8 8 0 0 1 5.1 16zm3-8h-3a8 8 0 0 1 4.3-3.9A15 15 0 0 0 8.1 8zM12 20c-.8-1.2-1.5-2.5-1.9-4h3.8c-.4 1.5-1.1 2.8-1.9 4zm2.3-6H9.7a14 14 0 0 1 0-4h4.6a14 14 0 0 1 0 4zm.3 5.9a15 15 0 0 0 1.3-3.9h3a8 8 0 0 1-4.3 3.9zm1.7-5.9a16 16 0 0 0 0-4h3.4a8.2 8.2 0 0 1 0 4z"/></svg>
    www.vestalukchirurgie.com
  </div>
  <div class="contact__row row-address">
    <svg viewBox="0 0 20 24"><path d="M10 0a8 8 0 0 0-8 8c0 6 8 16 8 16s8-10 8-16a8 8 0 0 0-8-8zm0 11a3 3 0 1 1 0-6 3 3 0 0 1 0 6z"/></svg>
    <span>Lindenweg 17, Marbachtal<br>Rheinland-Pfalz</span>
  </div>
</section>

<section class="card card--brand">
  <div class="brand">
    <div class="brand__mark"></div>
    <p class="brand__name">VESTALUK<br>CHIRURGIE</p>
  </div>
</section>

</body>
</html>
```